Poster promoting the "Golden Sheaf Day"

The Allied Guild of Millers and Pastrymakers (AGMP) created the "Golden Sheaf Day" in 2006. It is celebreated each year together with the ORV "Common Table Day" on 16th October.
After using different posters for a few years, AGMP decided to settle on a permanent poster some time ago, in order to allow people to recognize the poster long-term.
Now, AGMP feels that this permanent poster needs an update and modernization, apart from including the new AGMP logo.
Requisits:
1. Must include the new AGMP logo
2. The poster should reflect the importance of bread in the world and convey an image of health, innovation and tradition.
3. One version with text, one version without text
4. Text version: one poster for each of the four official AGMP languages:
ENGLISH: Golden Sheaf Day / 16th October
GERMAN: Tag der Goldenen Garbe / 16. Oktober
SPANISH: Día de la Gavilla Dorada / 16 de Octubre
FRENCH: Journée de la Gerbe Dorée / 16 Octobre
5. Colours must be defined with RGB colour code.
AGMP will take a decision regarding the new poster design during the next meeting of its Marketing Commission on March 24th, 2015. Therefore, please submit your proposals by 18th March in order to allow for pre-selection and modification requests.
More about AGMP at www.alliedguildmp.org.

```html
<!DOCTYPE html>
<html lang="en">
<head>
<meta charset="utf-8">
<title>Golden Sheaf Day · 16th October</title>
<link rel="stylesheet" href="https://fonts.googleapis.com/css2?family=Playfair+Display:wght@700&family=Quicksand:wght@500;600&display=swap">
<style>
  :root {
    --paper: #ffffff;
    --ink-brown: #4a2c12;
    --crust-gold: #a8862f;
    --crust-light: #c9a94f;
    --crust-soft: rgba(184, 150, 66, 0.45);
    --crust-fade: rgba(255, 255, 255, 0);
    --logo-accent: #c9cff0;
  }

  * { margin: 0; padding: 0; box-sizing: border-box; }

  html, body {
    width: 1008px;
    height: 1200px;
    overflow: hidden;
    background: var(--paper);
  }

  .poster {
    position: relative;
    width: 1008px;
    height: 1200px;
    background: var(--paper);
  }

  .brand {
    position: absolute;
    top: 108px;
    left: 0;
    width: 100%;
    display: flex;
    justify-content: center;
    align-items: center;
    gap: 12px;
  }

  .brand__name {
    font-family: "Quicksand", sans-serif;
    font-weight: 600;
    font-size: 50px;
    line-height: 1;
    letter-spacing: 1px;
    color: var(--ink-brown);
  }

  .brand__dot {
    width: 24px;
    height: 24px;
    border-radius: 50%;
    background: var(--logo-accent);
  }

  .bread-artwork {
    position: absolute;
    top: 290px;
    left: 130px;
    width: 690px;
    height: 610px;
    background: radial-gradient(ellipse 50% 50% at 50% 48%,
      var(--crust-light) 0%,
      var(--crust-gold) 30%,
      var(--crust-soft) 62%,
      var(--crust-fade) 100%);
  }

  .title {
    position: absolute;
    top: 1000px;
    left: 0;
    width: 100%;
    text-align: center;
    font-family: "Playfair Display", serif;
    font-weight: 700;
    font-size: 64px;
    line-height: 1.1;
    text-transform: uppercase;
    color: var(--ink-brown);
  }

  .date {
    position: absolute;
    top: 1088px;
    left: 0;
    width: 100%;
    text-align: center;
    font-family: "Quicksand", sans-serif;
    font-weight: 500;
    font-size: 40px;
    line-height: 1.1;
    color: var(--ink-brown);
  }
</style>
</head>
<body>
  <main class="poster">
    <header class="brand">
      <span class="brand__name">AGMP</span>
      <span class="brand__dot"></span>
    </header>

    <div class="bread-artwork" role="img"
         aria-label="Photograph of toasted bread pieces laid out on white like a sunburst: a round bread globe in the centre, surrounded by scattered bread cut-outs of a heart, a wheat ear, stars and short rays"></div>

    <h1 class="title">Golden Sheaf Day</h1>
    <p class="date">16th October</p>
  </main>
</body>
</html>
```